Very Simple/Minimal Business Card Design Project

The company operates in the industrial maritime infrastructure sector in Brazil. You can find more information on our website www.navelquor.com.br WE NEED TO LOOK POWERFUL AND SERIOUS
I have attached a copy of the old cards. We would like something more professional / industrial / sexy that also includes the position.

The card can be double sided or not. We would like you to propose as many options.

Thank you
Updates

Many thanks, do let me know if you have any questions. I am under a lot of time pressure to try and have them printed over the next days or so.

Please could you use the following information

for the address: Rua Tapiraçu, 418 - Centro, Rio de Janeiro, 20135-070, Brasil

for the mobile: +55 21 8372 9041
for the landline: +55 21 4067 3859

and position:  Diretor Geral

Thakn you

Target Market(s)

Shipowners, bankers, industrial companies

Industry/Entity Type

Industrial

Requirements
Must have
• POWERFUL
SERIOUS
SOLID
BIG CORPORATION

```html
<!DOCTYPE html>
<html lang="pt">
<head>
<meta charset="utf-8">
<title>Navelquor – Business Card</title>
<link rel="stylesheet" href="https://fonts.googleapis.com/css2?family=PT+Sans:wght@400;700&display=swap">
<style>
  :root {
    --navy: #1b2a78;
    --green: #2e9a3a;
    --green-dark: #1f6e27;
    --green-bright: #3bb54a;
    --paper: #ffffff;
    --paper-shade: #dcdcdc;
    --ink: #1a1a1a;
    --white: #ffffff;
  }
  html, body {
    margin: 0;
    padding: 0;
    width: 1200px;
    height: 800px;
    overflow: hidden;
    background: var(--paper);
  }
  .card {
    position: relative;
    width: 1200px;
    height: 800px;
    overflow: hidden;
    font-family: "PT Sans", sans-serif;
  }
  .card-shapes {
    position: absolute;
    inset: 0;
  }
  .brand {
    position: absolute;
    left: 107px;
    top: 67px;
    display: flex;
    align-items: center;
    gap: 16px;
  }
  .brand-mark {
    width: 146px;
    height: 133px;
    background: var(--green);
  }
  .brand-name {
    font-size: 92px;
    font-weight: 700;
    color: var(--navy);
    letter-spacing: 1px;
    line-height: 1;
  }
  .person {
    position: absolute;
    left: 101px;
    top: 232px;
    color: var(--ink);
  }
  .person-name {
    margin: 0;
    font-size: 58px;
    font-weight: 400;
    line-height: 1.1;
  }
  .person-role {
    margin: 4px 0 0;
    font-size: 40px;
    line-height: 1.1;
  }
  .contact {
    position: absolute;
    top: 537px;
    margin: 0;
    font-style: normal;
    font-size: 30px;
    line-height: 40px;
    color: var(--white);
  }
  .contact-address { left: 101px; }
  .contact-lines { left: 680px; }
</style>
</head>
<body>
<div class="card">
  <svg class="card-shapes" width="1200" height="800" viewBox="0 0 1200 800" aria-hidden="true">
    <defs>
      <linearGradient id="paperFade" x1="0" y1="0" x2="1" y2="1">
        <stop offset="0" stop-color="var(--paper)"/>
        <stop offset="1" stop-color="var(--paper-shade)"/>
      </linearGradient>
      <linearGradient id="greenFade" x1="0" y1="1" x2="1" y2="0">
        <stop offset="0" stop-color="var(--green-bright)"/>
        <stop offset="1" stop-color="var(--green-dark)"/>
      </linearGradient>
    </defs>
    <rect width="1200" height="800" fill="url(#paperFade)"/>
    <polygon points="0,485 706,485 541,800 0,800" fill="url(#greenFade)"/>
    <polygon points="960,0 1040,0 621,800 541,800" fill="var(--green-bright)"/>
    <polygon points="1040,0 1200,0 1200,800 621,800" fill="var(--navy)"/>
  </svg>

  <header class="brand">
    <span class="brand-mark"></span>
    <span class="brand-name">NAVELQUOR</span>
  </header>

  <section class="person">
    <h1 class="person-name">Tomas Ferrell</h1>
    <p class="person-role">Diretor Geral</p>
  </section>

  <address class="contact contact-address">
    Address: Rua Tapiraçu,<br>
    418 - Centro, Rio de Janeiro,<br>
    20135-070,<br>
    Brasil
  </address>

  <address class="contact contact-lines">
    landline: +55 21 4067 3859<br>
    Mobile: +55 21 8372 9041<br>
    E-mail: tomas@navelquor.com.br<br>
    www.navelquor.com.br
  </address>
</div>
</body>
</html>
```